PowerPoint Template for Meridian Liaison Hub. Website is www.meridianliaisonhub.example

The tagline for the Center is "Connecting the brightest minds in healthcare"

```html
<!DOCTYPE html>
<html lang="en">
<head>
<meta charset="utf-8">
<title>Meridian Liaison Hub – Presentation Template</title>
<link rel="stylesheet" href="https://fonts.googleapis.com/css2?family=Exo+2:ital,wght@0,500;0,600;0,700;1,600&family=Open+Sans:wght@400;600&display=swap">
<style>
  :root{
    --board:#cfcfcf;
    --slide:#ffffff;
    --navy:#0f3b6e;
    --sky:#1f6fc5;
    --grey:#b9b9b9;
    --grey-text:#8d8d8d;
    --rule:#8f8f8f;
    --label:#2e2e2e;
  }
  *{margin:0;padding:0;box-sizing:border-box}
  html,body{width:1200px;height:518px;overflow:hidden;background:var(--board)}
  .board{position:relative;width:1200px;height:518px}
  .slide{position:absolute;width:366px}
  .slide svg{display:block;width:366px;height:206px;background:var(--slide);box-shadow:0 1px 4px rgba(0,0,0,.35)}
  .slide-label{margin-top:10px;text-align:center;font:400 13px "Open Sans",sans-serif;color:var(--label);letter-spacing:.2px}
  .slide--cover{left:218px;top:16px}
  .slide--p1{left:616px;top:16px}
  .slide--p2{left:21px;top:266px}
  .slide--p3{left:418px;top:266px}
  .slide--p4{left:814px;top:266px}

  .navy{fill:var(--navy)} .sky{fill:var(--sky)} .grey{fill:var(--grey)}
  .rule{stroke:var(--rule);stroke-width:.8}
  .brand{font:600 9px "Exo 2",sans-serif;fill:var(--navy)}
  .brand--large{font-size:13px}
  .tagline{font:italic 600 13.5px "Exo 2",sans-serif;letter-spacing:.3px}
  .tagline--grey{fill:var(--grey-text)} .tagline--navy{fill:var(--navy)}
  .title{font:700 27px "Exo 2",sans-serif}
  .title--wide{font:600 19px "Exo 2",sans-serif;letter-spacing:4.5px}
  .t-navy{fill:var(--navy)} .t-grey{fill:var(--grey-text)}
  .web{font:400 6px "Open Sans",sans-serif;fill:var(--grey-text);letter-spacing:.8px}
  .page-no{font:400 5.5px "Open Sans",sans-serif;fill:#555;letter-spacing:1px}
  .body-navy{font:400 5.6px "Open Sans",sans-serif;fill:var(--navy)}
  .body-grey{font:400 5.6px "Open Sans",sans-serif;fill:var(--grey-text)}
  .sub-head{font:700 8px "Exo 2",sans-serif;fill:var(--navy)}
  .list-item{font:400 5.8px "Open Sans",sans-serif;fill:#222}
</style>
</head>
<body>
<main class="board">

  <!-- Cover -->
  <figure class="slide slide--cover">
    <svg viewBox="0 0 457 258">
      <defs>
        <linearGradient id="tone-clinic" x1="0" y1="0" x2="1" y2="1"><stop offset="0" stop-color="#9aaeb2"/><stop offset="1" stop-color="#5f7076"/></linearGradient>
        <linearGradient id="tone-lab" x1="0" y1="0" x2="1" y2="1"><stop offset="0" stop-color="#d2d4d7"/><stop offset="1" stop-color="#3c3f44"/></linearGradient>
        <linearGradient id="tone-desk" x1="0" y1="0" x2="1" y2="1"><stop offset="0" stop-color="#c8d7dd"/><stop offset="1" stop-color="#93a8b2"/></linearGradient>
        <linearGradient id="tone-supplies" x1="0" y1="0" x2="1" y2="1"><stop offset="0" stop-color="#ececec"/><stop offset="1" stop-color="#b3b6ba"/></linearGradient>
        <linearGradient id="tone-care" x1="0" y1="0" x2="1" y2="1"><stop offset="0" stop-color="#b0a393"/><stop offset="1" stop-color="#6d7a8c"/></linearGradient>
      </defs>
      <polygon role="img" aria-label="Photo: hands measuring a patient's blood pressure" fill="url(#tone-clinic)" points="0,0 155,0 232,138 170,258 0,258"/>
      <polygon class="navy" points="168,0 188,0 266,140 246,140"/>
      <polygon class="navy" points="246,140 266,140 198,258 178,258"/>
      <polygon class="sky" points="292,96 310,96 278,152 260,152"/>
      <polygon class="grey" points="298,140 316,140 306,155 288,155"/>
      <polygon class="grey" points="322,140 340,140 330,155 312,155"/>
      <polygon class="grey" points="248,158 346,158 336,172 238,172"/>
      <polygon class="navy" points="346,122 457,122 457,150 330,150"/>
      <text class="tagline tagline--grey" x="450" y="58" text-anchor="end">CONNECTING THE BRIGHTEST</text>
      <text class="tagline tagline--navy" x="450" y="77" text-anchor="end">MINDS IN HEALTHCARE</text>
      <circle class="navy" cx="306" cy="222" r="10"/>
      <text class="brand brand--large" x="321" y="227">Meridian Liaison Hub</text>
      <line class="rule" x1="182" y1="246" x2="282" y2="246"/>
      <text class="web" x="450" y="248" text-anchor="end">www.meridianliaisonhub.example</text>
    </svg>
    <figcaption class="slide-label">COVER PAGE</figcaption>
  </figure>

  <!-- Page 01 -->
  <figure class="slide slide--p1">
    <svg viewBox="0 0 457 258">
      <circle class="navy" cx="16" cy="24" r="6"/>
      <text class="brand" x="26" y="27">Meridian Liaison Hub</text>
      <polygon class="grey" points="130,12 148,12 132,42 114,42"/>
      <polygon class="grey" points="154,12 172,12 156,42 138,42"/>
      <rect class="grey" x="0" y="46" width="182" height="5"/>
      <text class="title" x="225" y="92" text-anchor="middle"><tspan class="t-navy">LOREM </tspan><tspan class="t-grey">IPSUM</tspan></text>
      <polygon role="img" aria-label="Photo: gloved hands handling a sample tube in a laboratory" fill="url(#tone-lab)" points="0,98 404,98 330,258 0,258"/>
      <polygon class="grey" points="410,98 420,98 346,258 336,258"/>
      <polygon class="navy" points="428,30 470,30 366,258 324,258"/>
      <line class="rule" x1="368" y1="246" x2="430" y2="246"/>
      <text class="page-no" x="438" y="248">01</text>
    </svg>
    <figcaption class="slide-label">PAGE - 01</figcaption>
  </figure>

  <!-- Page 02 -->
  <figure class="slide slide--p2">
    <svg viewBox="0 0 457 258">
      <circle class="navy" cx="16" cy="24" r="6"/>
      <text class="brand" x="26" y="27">Meridian Liaison Hub</text>
      <polygon class="grey" points="130,12 148,12 132,42 114,42"/>
      <polygon class="grey" points="154,12 172,12 156,42 138,42"/>
      <rect class="grey" x="0" y="46" width="182" height="5"/>
      <text class="title--wide" x="222" y="42"><tspan class="t-navy">LOREM </tspan><tspan class="t-grey">IPSUM</tspan></text>
      <text class="body-navy">
        <tspan x="10" y="98">Lorem Ipsum is simply dummy text of the printing and typesetting</tspan>
        <tspan x="10" y="106">industry. Lorem Ipsum has been the industry's standard dummy text</tspan>
        <tspan x="10" y="114">ever since the 1500s</tspan>
      </text>
      <rect class="navy" x="0" y="135" width="4" height="14"/>
      <text class="sub-head" x="10" y="145">LOREM IPSUM</text>
      <text class="body-grey">
        <tspan x="10" y="164">Lorem Ipsum is simply dummy text of the printing and</tspan>
        <tspan x="10" y="172">typesetting industry. Lorem Ipsum has been the industry's</tspan>
        <tspan x="10" y="180">standard dummy text ever since the 1500s</tspan>
      </text>
      <polygon role="img" aria-label="Photo: laptop, stethoscope and glasses on a desk" fill="url(#tone-desk)" points="218,72 457,72 457,235 145,235"/>
      <line class="rule" x1="0" y1="246" x2="430" y2="246"/>
      <text class="page-no" x="438" y="248">02</text>
    </svg>
    <figcaption class="slide-label">PAGE - 02</figcaption>
  </figure>

  <!-- Page 03 -->
  <figure class="slide slide--p3">
    <svg viewBox="0 0 457 258">
      <circle class="navy" cx="16" cy="24" r="6"/>
      <text class="brand" x="26" y="27">Meridian Liaison Hub</text>
      <polygon class="grey" points="130,12 148,12 132,42 114,42"/>
      <polygon class="grey" points="154,12 172,12 156,42 138,42"/>
      <rect class="grey" x="0" y="46" width="182" height="5"/>
      <text class="title" x="188" y="84" text-anchor="middle"><tspan class="t-navy">LOREM </tspan><tspan class="t-grey">IPSUM</tspan></text>
      <polygon role="img" aria-label="Photo: glucose meter, insulin syringe and test strips" fill="url(#tone-supplies)" points="0,92 408,92 332,258 0,258"/>
      <polygon class="grey" points="414,92 424,92 348,258 338,258"/>
      <polygon class="navy" points="432,30 474,30 370,258 328,258"/>
      <line class="rule" x1="372" y1="246" x2="430" y2="246"/>
      <text class="page-no" x="438" y="248">03</text>
    </svg>
    <figcaption class="slide-label">PAGE - 03</figcaption>
  </figure>

  <!-- Page 04 -->
  <figure class="slide slide--p4">
    <svg viewBox="0 0 457 258">
      <circle class="navy" cx="16" cy="24" r="6"/>
      <text class="brand" x="26" y="27">Meridian Liaison Hub</text>
      <polygon class="grey" points="130,12 148,12 132,42 114,42"/>
      <polygon class="grey" points="154,12 172,12 156,42 138,42"/>
      <rect class="grey" x="0" y="46" width="182" height="5"/>
      <text class="title--wide" x="200" y="38"><tspan class="t-navy">LOREM </tspan><tspan class="t-grey">IPSUM</tspan></text>
      <polyline points="404,31 420,31 420,210 408,210" fill="none" class="rule"/>
      <polygon role="img" aria-label="Photo: patient walking with a frame" fill="url(#tone-care)" points="72,74 184,74 162,140 50,140"/>
      <polygon role="img" aria-label="Photo: clinician preparing medicines" fill="url(#tone-supplies)" points="192,74 292,74 270,140 170,140"/>
      <polygon role="img" aria-label="Photo: doctor typing on a laptop beside a stethoscope" fill="url(#tone-desk)" points="10,148 246,148 222,216 10,216"/>
      <g class="checklist">
        <g><line class="rule" x1="408" y1="66" x2="420" y2="66"/><circle class="navy" cx="406" cy="66" r="3"/><text class="list-item" x="398" y="68" text-anchor="end">Lorem Ipsum is simply</text></g>
        <g><line class="rule" x1="408" y1="95" x2="420" y2="95"/><circle class="navy" cx="406" cy="95" r="3"/><text class="list-item" x="398" y="97" text-anchor="end">Dummy text of the printing</text></g>
        <g><line class="rule" x1="408" y1="124" x2="420" y2="124"/><circle class="navy" cx="406" cy="124" r="3"/><text class="list-item" x="398" y="126" text-anchor="end">Typesetting industry</text></g>
        <g><line class="rule" x1="408" y1="152" x2="420" y2="152"/><circle class="navy" cx="406" cy="152" r="3"/><text class="list-item" x="398" y="154" text-anchor="end">Lorem Ipsum is simply</text></g>
        <g><line class="rule" x1="408" y1="181" x2="420" y2="181"/><circle class="navy" cx="406" cy="181" r="3"/><text class="list-item" x="398" y="183" text-anchor="end">Dummy text of the printing</text></g>
        <g><circle class="navy" cx="406" cy="210" r="3"/><text class="list-item" x="398" y="212" text-anchor="end">Typesetting industry</text></g>
      </g>
      <line class="rule" x1="0" y1="246" x2="430" y2="246"/>
      <text class="page-no" x="438" y="248">04</text>
    </svg>
    <figcaption class="slide-label">PAGE - 04</figcaption>
  </figure>

</main>
</body>
</html>
```